Electrical Engineering Business Card Design

I need a business card design for an engineering consulting company based in Orlando, FL. I have had a logo created which the files are attached. We work primarily in the theme park and entertainment market sector but do projects in all market sectors. We have been serving Central Florida since 1994 and continue to strive to serve our clients and provide outstanding designs.
Theme Park

```html
<!DOCTYPE html>
<html lang="en">
<head>
<meta charset="utf-8">
<title>Voltaro Associates – Business Card</title>
<link rel="stylesheet" href="https://fonts.googleapis.com/css2?family=Oswald:wght@500&family=Open+Sans:wght@400;600&display=swap">
<style>
  :root {
    --green: #8cc63f;
    --green-light: #b5dc5c;
    --grey-text: #5a5a5a;
    --dark-text: #555759;
    --white: #ffffff;
    --card-white: #f7f7f7;
    --stage: #e9e9e6;
  }
  html, body {
    margin: 0;
    width: 1200px;
    height: 1023px;
    overflow: hidden;
    background: var(--stage);
  }
  .canvas {
    position: relative;
    width: 1200px;
    height: 1023px;
  }
  .card {
    position: absolute;
    left: 340px;
    width: 520px;
    height: 297px;
    overflow: hidden;
    box-shadow: 0 4px 14px rgba(0,0,0,0.18);
  }
  .card--front { top: 120px; background: var(--card-white); }
  .card--back  { top: 570px; background: linear-gradient(135deg, var(--green-light), var(--green)); }
  .card__band { position: absolute; inset: 0; }

  .brand {
    position: absolute;
    display: flex;
    align-items: center;
    gap: 10px;
  }
  .brand__mark { width: 14px; height: 14px; background: var(--green); }
  .brand__name {
    font-family: "Oswald", sans-serif;
    font-weight: 500;
    color: var(--dark-text);
    letter-spacing: 0.5px;
  }
  .brand__place {
    position: absolute;
    font-family: "Open Sans", sans-serif;
    font-weight: 600;
    letter-spacing: 4px;
    color: var(--dark-text);
  }
  .card--front .brand { left: 44px; top: 86px; }
  .card--front .brand__name { font-size: 30px; }
  .card--front .brand__place { left: 68px; top: 130px; font-size: 11px; }

  .person { position: absolute; left: 44px; top: 190px; font-family: "Open Sans", sans-serif; }
  .person__name { font-size: 17px; font-weight: 600; color: var(--green-light); text-transform: uppercase; margin: 0; }
  .person__role { font-size: 11px; color: var(--grey-text); margin: 0 0 8px; }
  .contact { list-style: none; margin: 0; padding: 0; }
  .contact__item {
    display: flex; align-items: center; gap: 7px;
    font-size: 11px; color: var(--grey-text); line-height: 17px;
  }
  .contact__icon { width: 11px; height: 11px; }

  .divider { position: absolute; left: 330px; top: 150px; width: 1px; height: 46px; background: var(--green); }
  .address {
    position: absolute; left: 352px; top: 148px; margin: 0;
    font-family: "Open Sans", sans-serif; font-size: 11px; line-height: 17px;
    color: var(--grey-text); font-style: normal;
  }

  .card--back .brand { left: 56px; top: 104px; }
  .card--back .brand__mark { background: var(--white); width: 22px; height: 22px; }
  .card--back .brand__name { color: var(--white); font-size: 40px; }
  .card--back .brand__place { color: var(--white); left: 90px; top: 166px; font-size: 13px; }
</style>
</head>
<body>
<main class="canvas">

  <section class="card card--front" aria-label="Card front">
    <svg class="card__band" viewBox="0 0 520 297" aria-hidden="true">
      <polygon points="400,0 520,0 520,100" fill="var(--green)"/>
      <polygon points="360,0 400,0 520,100 520,130" fill="var(--green-light)" opacity="0.55"/>
    </svg>

    <div class="brand">
      <span class="brand__mark"></span>
      <span class="brand__name">Voltaro Associates, P.A.</span>
    </div>
    <span class="brand__place">ORLANDO, FLORIDA</span>

    <div class="person">
      <p class="person__name">Dana Whitfield</p>
      <p class="person__role">Director</p>
      <ul class="contact">
        <li class="contact__item">
          <svg class="contact__icon" viewBox="0 0 12 12"><circle cx="6" cy="6" r="6" fill="var(--green-light)"/><path d="M4 3.2l1 1.4-.6.7a4 4 0 0 0 2.3 2.3l.7-.6 1.4 1-.6 1a5 5 0 0 1-5.2-5.2z" fill="var(--white)"/></svg>
          407-555-0148
        </li>
        <li class="contact__item">
          <svg class="contact__icon" viewBox="0 0 12 12"><circle cx="6" cy="6" r="6" fill="var(--green-light)"/><rect x="4.2" y="2.6" width="3.6" height="6.8" rx="0.7" fill="var(--white)"/></svg>
          407-555-0193
        </li>
        <li class="contact__item">
          <svg class="contact__icon" viewBox="0 0 12 12"><circle cx="6" cy="6" r="6" fill="var(--green-light)"/><rect x="3" y="4" width="6" height="4.2" fill="var(--white)"/><path d="M3 4l3 2.3L9 4" stroke="var(--green-light)" stroke-width="0.7" fill="none"/></svg>
          dana@voltaroassoc.com
        </li>
      </ul>
    </div>

    <span class="divider"></span>
    <address class="address">PO Box 104422<br>Orlando, FL 32802</address>
  </section>

  <section class="card card--back" aria-label="Card back">
    <svg class="card__band" viewBox="0 0 520 297" aria-hidden="true">
      <polygon points="520,150 520,297 370,297" fill="var(--card-white)"/>
    </svg>
    <div class="brand">
      <span class="brand__mark"></span>
      <span class="brand__name">Voltaro Associates, P.A.</span>
    </div>
    <span class="brand__place">ORLANDO, FLORIDA</span>
  </section>

</main>
</body>
</html>
```